Blog based website for baseball.

I am a college baseball coach looking to create a blog type site that uses content to keep readers coming back and eventually trusting me enough to buy my products.

I am an author, coach, writer, speaker with a bunch sites now, but I want to make one main site that people can come back to and see new content over and over..

Target Market(s)

High school baseball players and parents.

Industry/Entity Type

Education

Number of Pages Required

4 page

Font styles to use
Sans Serif

Requirements
Must have
• 1) An about page. 2) Either commerce page or link to my other commerce pages. 3) Featured blog but also access to past blogs. 4) Featured product of the week (maybe in side bar). 5) Places to opt in and join the list. 6) A way to share the content people like.
Nice to have
• No idea the difference between uncoded and coded!
• I like the idea of an opt in pop up.

```html
<!DOCTYPE html>
<html lang="en">
<head>
<meta charset="utf-8">
<title>Diamond Prep Baseball</title>
<link rel="stylesheet" href="https://fonts.googleapis.com/css2?family=Open+Sans:wght@400;600;700&family=Rubik:wght@500;700&display=swap">
<style>
:root{
  --red:#e0000f;
  --red-dark:#a8000a;
  --ink:#222;
  --muted:#8a8a8a;
  --line:#e3e3e3;
  --page:#f1f1f1;
  --card:#ffffff;
  --footer:#2f2f2f;
  --navy:#1e3a7a;
}
*{box-sizing:border-box;margin:0;padding:0}
html,body{width:1200px;height:2184px;overflow:hidden}
body{font-family:"Open Sans",sans-serif;color:var(--ink);background:var(--page);position:relative}
.abs{position:absolute}

/* header */
.site-header{left:0;top:0;width:1200px;height:135px;background:linear-gradient(#e6e8ec,#f2f3f5)}
.brand{left:182px;top:40px;display:flex;align-items:center;gap:10px}
.brand-dot{width:40px;height:40px;border-radius:50%;background:var(--red)}
.brand-name{font-family:"Rubik",sans-serif;font-weight:700;font-size:22px;color:var(--navy);line-height:1}
.login{left:884px;top:59px;font-size:11px;color:#c8c8c8;letter-spacing:.5px}
.btn-signup{left:943px;top:50px;width:76px;height:33px;background:var(--red);color:#fff;font-size:10px;display:flex;align-items:center;justify-content:center;border-radius:2px;box-shadow:0 1px 2px rgba(0,0,0,.3)}

.main-nav{left:0;top:135px;width:1200px;height:54px;background:linear-gradient(#f0101c,#c9000b);display:flex;align-items:center;padding-left:179px}
.main-nav a{color:#fff;text-decoration:none;font-size:16px;letter-spacing:.3px;margin-right:53px}

/* hero */
.hero{left:0;top:189px;width:1200px;height:338px;background:linear-gradient(180deg,#6e5a3a 0,#3a3029 45%,#1d1a18 100%)}
.hero-caption{left:180px;top:261px;width:839px;height:77px;background:rgba(0,0,0,.78);padding:14px 21px;color:#fff}
.hero-caption h2{font-weight:400;font-size:21px;margin-bottom:6px}
.hero-caption p{font-size:12px;color:#ddd}
.hero-arrows{right:21px;top:28px}

/* background feature */
.backdrop{left:0;top:527px;width:597px;height:754px;opacity:.55;background:linear-gradient(160deg,#ccd1dc 0,#e4e2de 55%,#f1f1f1 100%)}

/* posts */
.post{left:180px;width:526px;background:var(--card);box-shadow:0 0 2px rgba(0,0,0,.06)}
.post-media{height:204px}
.post-body{padding:22px 14px 0}
.post-title{font-family:"Rubik",sans-serif;font-weight:700;font-size:20px;line-height:21px;color:#111;max-width:450px}
.post-meta{margin-top:18px;font-size:12px;color:#555;display:flex;align-items:center;gap:6px}
.post-meta .sep{color:#999;margin:0 4px}
.post-excerpt{margin-top:18px;font-size:10.5px;line-height:20px;color:#9a9a9a;padding-left:5px;width:470px}
.btn-red{display:inline-flex;align-items:center;justify-content:center;background:linear-gradient(var(--red),var(--red-dark));color:#fff;border-radius:3px;font-size:11px;box-shadow:0 1px 2px rgba(0,0,0,.3)}
.post .btn-red{margin-top:22px;margin-left:3px;width:73px;height:34px}

.pager{left:180px;top:2060px;display:flex;gap:10px}
.pager span{height:26px;min-width:26px;padding:0 8px;background:#fff;border:1px solid #ddd;font-size:11px;font-weight:600;display:flex;align-items:center;justify-content:center;color:#333}

/* sidebar */
.sidebar{left:750px;top:560px;width:268px;height:1486px;background:var(--card)}
.widget-title{font-size:15px;font-weight:400;color:#222}
.sb{position:absolute;left:18px;width:232px}
.field{height:41px;border:1px solid #ddd;font-size:10px;color:#333;display:flex;align-items:center;padding-left:9px;gap:8px}
.social-grid{display:flex;flex-wrap:wrap;gap:4px;width:232px}
.social-grid i{width:20px;height:20px;background:#d6d6d6;border-radius:2px;display:block}
.product{position:absolute;left:18px;display:flex;gap:16px}
.product-img{width:89px;height:89px}
.product h4{font-weight:400;font-size:14px;margin-top:3px}
.product .btn-dark{margin-top:18px;width:74px;height:34px;background:linear-gradient(#444,#111);color:#fff;font-size:11px;display:flex;align-items:center;justify-content:center;border-radius:3px}
.cat-list{list-style:none}
.cat-list li{height:31px;border-bottom:1px solid #ececec;font-size:11px;color:#666;display:flex;align-items:center}
.fan-grid{display:grid;grid-template-columns:repeat(5,44px);width:220px}
.fan-grid div{height:44px}

/* footer */
.site-footer{left:0;top:2102px;width:1200px;height:82px;background:var(--footer)}
.foot-nav{left:180px;top:26px;display:flex;gap:26px}
.foot-nav a{color:#ccc;font-size:10px;text-decoration:none}
.copyright{left:180px;top:48px;font-size:10px;color:#aaa}
.foot-social{left:744px;top:30px;display:flex;gap:15px}
.foot-social i{width:20px;height:20px;display:block;border-radius:2px}
</style>
</head>
<body>

<header class="site-header abs">
  <div class="brand abs"><span class="brand-dot"></span><span class="brand-name">Diamond Prep</span></div>
  <div class="login abs">LOGIN</div>
  <div class="btn-signup abs">SIGN UP</div>
</header>

<nav class="main-nav abs">
  <a href="#">HOME</a><a href="#">ABOUT US</a><a href="#">VENUES</a><a href="#">PROGRAMS</a><a href="#">EVENTS</a><a href="#">NEWS</a><a href="#">CONTACT</a>
</nav>

<section class="hero abs" role="img" aria-label="Batter in a red helmet under stadium lights">
  <div class="hero-caption abs">
    <h2>Baseball coaching</h2>
    <p>Neque porro quisquam est qui dolorem ipsum quia dolor sit amet, consectetur, adipisci velit...</p>
    <svg class="hero-arrows abs" width="22" height="14" viewBox="0 0 22 14"><path d="M7 2 2 7l5 5M15 2l5 5-5 5" fill="none" stroke="#fff" stroke-width="1.8"/></svg>
  </div>
</section>

<div class="backdrop abs" role="img" aria-label="Faded recruiting guide book cover"></div>

<article class="post abs" style="top:560px;height:477px">
  <div class="post-media" role="img" aria-label="Team boarding a plane" style="background:linear-gradient(#dcdee2,#a9acae)"></div>
  <div class="post-body">
    <h3 class="post-title">Ridgeview baseball pitching coach Dale Harmon sits down with Ray</h3>
    <div class="post-meta">Share <svg width="11" height="9" viewBox="0 0 11 9"><path d="M6 0l5 4-5 4V5.5C3 5.5 1 6.5 0 9c0-4 2-6 6-6.5z" fill="#555"/></svg><span class="sep">|</span>Like <svg width="10" height="9" viewBox="0 0 10 9"><path d="M0 4h2v5H0zM3 4l2-4c1 0 1.5.6 1.3 1.6L6 3.5h3c.7 0 1 .6.9 1.2L9 8.2c-.1.5-.5.8-1 .8H3z" fill="#555"/></svg></div>
    <p class="post-excerpt">Nemo enim ipsam voluptatem quia voluptas sit aspernatur aut odit aut fugit, sed quia consequuntur magni dolores eos qui ratione voluptatem sequi nesciunt. Neque porro quisquam est, qui dolorem ipsum quia dolor sit amet, consectetur, adipisci velit, sed quia non numquam eius modi tempora incidunt</p>
    <span class="btn-red">Read More</span>
  </div>
</article>

<article class="post abs" style="top:1073px;height:457px">
  <div class="post-media" role="img" aria-label="Championship team celebrating on the field" style="background:linear-gradient(#9aa0aa,#b8393f)"></div>
  <div class="post-body">
    <h3 class="post-title">Free Baseball Recruiting Book to the 1st 10</h3>
    <div class="post-meta">Share <svg width="11" height="9" viewBox="0 0 11 9"><path d="M6 0l5 4-5 4V5.5C3 5.5 1 6.5 0 9c0-4 2-6 6-6.5z" fill="#555"/></svg><span class="sep">|</span>Like <svg width="10" height="9" viewBox="0 0 10 9"><path d="M0 4h2v5H0zM3 4l2-4c1 0 1.5.6 1.3 1.6L6 3.5h3c.7 0 1 .6.9 1.2L9 8.2c-.1.5-.5.8-1 .8H3z" fill="#555"/></svg></div>
    <p class="post-excerpt">Nemo enim ipsam voluptatem quia voluptas sit aspernatur aut odit aut fugit, sed quia consequuntur magni dolores eos qui ratione voluptatem sequi nesciunt. Neque porro quisquam est, qui dolorem ipsum quia dolor sit amet, consectetur, adipisci velit, sed quia non numquam eius modi tempora incidunt</p>
    <span class="btn-red">Read More</span>
  </div>
</article>

<article class="post abs" style="top:1568px;height:478px">
  <div class="post-media" role="img" aria-label="Aerial view of a baseball diamond with crowd" style="background:linear-gradient(#5b7c3c,#3d5a3a)"></div>
  <div class="post-body">
    <h3 class="post-title" style="max-width:420px">A few spots remain for this Monday's Elite Pitcher Boot Camp.</h3>
    <div class="post-meta">Share <svg width="11" height="9" viewBox="0 0 11 9"><path d="M6 0l5 4-5 4V5.5C3 5.5 1 6.5 0 9c0-4 2-6 6-6.5z" fill="#555"/></svg><span class="sep">|</span>Like <svg width="10" height="9" viewBox="0 0 10 9"><path d="M0 4h2v5H0zM3 4l2-4c1 0 1.5.6 1.3 1.6L6 3.5h3c.7 0 1 .6.9 1.2L9 8.2c-.1.5-.5.8-1 .8H3z" fill="#555"/></svg></div>
    <p class="post-excerpt">Nemo enim ipsam voluptatem quia voluptas sit aspernatur aut odit aut fugit, sed quia consequuntur magni dolores eos qui ratione voluptatem sequi nesciunt. Neque porro quisquam est, qui dolorem ipsum quia dolor sit amet, consectetur, adipisci velit, sed quia non numquam eius modi tempora incidunt</p>
    <span class="btn-red">Read More</span>
  </div>
</article>

<nav class="pager abs">
  <span>Prev</span><span>1</span><span>2</span><span>3</span><span>4</span><span>5</span><span>6</span><span>...</span><span>22</span><span>Next</span>
</nav>

<aside class="sidebar abs">
  <div class="sb" style="top:16px;left:22px">
    <h3 class="widget-title">join the Mail list.</h3>
    <p style="font-size:9px;color:var(--muted);margin-top:6px;width:225px">subscribe to our monthly news updates in your mail address</p>
  </div>
  <div class="sb field" style="top:82px">Enter Your Mail Id</div>
  <div class="sb" style="top:137px"><span class="btn-red" style="width:56px;height:30px;font-size:10px">SUBMIT</span></div>

  <h3 class="sb widget-title" style="top:196px">Connect With US</h3>
  <div class="sb social-grid" style="top:232px">
    <i></i><i></i><i></i><i></i><i></i><i></i><i></i><i></i><i></i><i></i><i></i><i></i><i></i><i></i><i></i>
  </div>

  <h3 class="sb widget-title" style="top:316px">Featured product</h3>
  <div class="product" style="top:356px"><div class="product-img" role="img" aria-label="Coaches at an event" style="background:linear-gradient(#8b8f96,#4d5158)"></div><div><h4>Lorem ipsum</h4><div class="btn-dark">Buy Now</div></div></div>
  <div class="product" style="top:451px"><div class="product-img" role="img" aria-label="Night game under lights" style="background:linear-gradient(#3a3022,#7a5a2e)"></div><div><h4>Lorem ipsum</h4><div class="btn-dark">Buy Now</div></div></div>
  <div class="product" style="top:547px"><div class="product-img" role="img" aria-label="Outfield grass and fence" style="background:linear-gradient(#8e9aa3,#4f6b3b)"></div><div><h4>Lorem ipsum</h4><div class="btn-dark">Buy Now</div></div></div>

  <h3 class="sb widget-title" style="top:662px">Find anything</h3>
  <div class="sb field" style="top:698px"><svg width="11" height="11" viewBox="0 0 11 11"><circle cx="4.5" cy="4.5" r="3.5" fill="none" stroke="#999" stroke-width="1.4"/><path d="M7 7l3.5 3.5" stroke="#999" stroke-width="1.4"/></svg></div>
  <div class="sb" style="top:752px"><span class="btn-red" style="width:56px;height:30px;font-size:10px">SEARCH</span></div>

  <h3 class="sb widget-title" style="top:816px">Category</h3>
  <ul class="sb cat-list" style="top:852px;width:234px">
    <li>Neque porro</li><li>quisquam est,</li><li>qui dolorem</li><li>ipsum quia dolor sit a</li><li>met, consectetur,</li><li>adipisci velit, sed</li><li>quia non numquam</li><li>eius modi tempora incidunt ut</li><li>labore et dolore magnam aliquam</li><li>quaerat voluptatem</li>
  </ul>

  <h3 class="sb widget-title" style="top:1177px">Fan Page</h3>
  <div class="sb" style="top:1206px;display:flex;gap:9px">
    <div style="width:44px;height:44px;background:var(--red)"></div>
    <div>
      <div style="font-size:10px;color:var(--navy)">diamondprep.com</div>
      <div style="margin-top:4px;width:42px;height:16px;background:#4b67a1;color:#fff;font-size:9px;display:flex;align-items:center;justify-content:center;border-radius:2px">Like</div>
    </div>
  </div>
  <div class="sb" style="top:1256px;font-size:8px;color:#333">135 people like diamondprep.com</div>
  <div class="sb fan-grid" style="top:1278px" role="img" aria-label="Grid of fan profile photos">
    <div style="background:#6a6a6a"></div><div style="background:#8b3a2e"></div><div style="background:#6b5a3a"></div><div style="background:#8a7f7a"></div><div style="background:#7a8a95"></div>
    <div style="background:#9a9a9a"></div><div style="background:#3a3030"></div><div style="background:#a88a6a"></div><div style="background:#6a7a8a"></div><div style="background:#9a7a6a"></div>
  </div>
  <div class="sb" style="top:1374px;border-top:1px solid #ddd;padding-top:6px;font-size:8px;color:#666;display:flex;align-items:center;gap:5px"><i style="width:9px;height:9px;background:#4b67a1;display:block"></i>Fan page plugin</div>
</aside>

<footer class="site-footer abs">
  <nav class="foot-nav abs"><a href="#">HOME</a><a href="#">ABOUT US</a><a href="#">VENUES</a><a href="#">PROGRAMS</a><a href="#">EVENTS</a><a href="#">NEWS</a><a href="#">CONTACT</a></nav>
  <div class="copyright abs">© 2015 All rights reserved.</div>
  <div class="foot-social abs">
    <i style="background:#f0a030"></i><i style="background:#3ab0e0"></i><i style="background:#d04a8a"></i><i style="background:#3b5ea0"></i><i style="background:#3ab0c8"></i><i style="background:#1a5fd0"></i><i style="background:#2a7ab0"></i><i style="background:#d02020"></i><i style="background:#10a8e0"></i>
  </div>
</footer>

</body>
</html>
```